Cafe Menu Required

We need a menu for our coffee shop.
I would like something very much the same as what I have attached.

I have attached a word doc with the items needed on the menu.

I have also attached our logo

I would like to print these on A3 size poster

Industry/Entity Type

Cafe

```html
<!DOCTYPE html>
<html lang="en">
<head>
<meta charset="utf-8">
<title>Ward Round Cafe – Beverage Menu</title>
<link href="https://fonts.googleapis.com/css2?family=Lato:wght@700;900&display=swap" rel="stylesheet">
<style>
  :root {
    --board-dark: #151515;
    --board-mid: #2a2a2a;
    --chalk: #f2f2f2;
    --brand-red: #d3202f;
    --text-white: #ffffff;
    --band-light: rgba(255,255,255,0.26);
    --band-soft: rgba(255,255,255,0.14);
  }
  html, body { margin: 0; padding: 0; overflow: hidden; background: var(--board-dark); }
  .menu-board {
    position: relative; width: 1200px; height: 849px; overflow: hidden;
    background: radial-gradient(ellipse at 50% 40%, var(--board-mid) 0%, var(--board-dark) 75%);
    font-family: 'Lato', sans-serif; color: var(--text-white);
  }
  .chalk-frame { position: absolute; inset: 0; }
  .brand {
    position: absolute; top: 70px; left: 0; width: 1200px;
    display: flex; justify-content: center; align-items: center; gap: 14px;
  }
  .brand-dot { width: 58px; height: 58px; border-radius: 50%; background: var(--brand-red); }
  .brand-name { font-size: 38px; font-weight: 900; color: var(--text-white); letter-spacing: 1px; }
  .tagline {
    position: absolute; top: 168px; left: 0; width: 1200px; text-align: center;
    font-size: 22px; font-weight: 900; color: var(--brand-red);
    text-shadow: -2px 0 #fff, 2px 0 #fff, 0 -2px #fff, 0 2px #fff, -1px -1px #fff, 1px 1px #fff, -1px 1px #fff, 1px -1px #fff;
  }
  .tagline .sep { color: var(--chalk); text-shadow: none; margin: 0 4px; }
  .menu-section { position: absolute; }
  .section-title { font-size: 28px; font-weight: 900; margin: 0 0 10px 11px; height: 30px; line-height: 30px; }
  .menu-list { list-style: none; margin: 0; padding: 0; }
  .menu-item {
    display: flex; justify-content: space-between; align-items: center;
    height: 31.7px; padding: 0 6px 0 11px; font-size: 23px; font-weight: 700;
    background: linear-gradient(90deg, var(--band-soft) 0%, rgba(255,255,255,0.04) 55%, var(--band-soft) 100%);
  }
  .menu-item:nth-child(odd) {
    background: linear-gradient(90deg, var(--band-light) 0%, rgba(255,255,255,0.08) 55%, var(--band-light) 100%);
  }
  .hot { left: 82px; top: 225px; width: 466px; }
  .extras { left: 655px; top: 225px; width: 465px; }
  .cold { left: 655px; top: 448px; width: 465px; }
  .social {
    position: absolute; left: 672px; top: 722px; display: flex; align-items: center; gap: 10px;
    font-size: 22px; font-weight: 900; color: var(--brand-red);
  }
  .social-dot { width: 30px; height: 30px; border-radius: 50%; background: var(--chalk); }
</style>
</head>
<body>
<main class="menu-board">
  <svg class="chalk-frame" width="1200" height="849" viewBox="0 0 1200 849" aria-hidden="true">
    <rect x="31" y="50" width="1138" height="750" fill="none" stroke="var(--chalk)" stroke-width="3" opacity="0.85"/>
    <rect x="46" y="40" width="1108" height="772" fill="none" stroke="var(--chalk)" stroke-width="3" opacity="0.85"/>
  </svg>

  <header class="brand">
    <span class="brand-dot"></span>
    <span class="brand-name">Ward Round Cafe</span>
  </header>
  <p class="tagline" style="margin:0">coffee<span class="sep">•</span>catering<span class="sep">•</span>food to go</p>

  <section class="menu-section hot">
    <h2 class="section-title" style="margin-top:0">Hot Beverages</h2>
    <ul class="menu-list">
      <li class="menu-item"><span>Espresso</span><span>3.5</span></li>
      <li class="menu-item"><span>Piccolo</span><span>3.5</span></li>
      <li class="menu-item"><span>Short Macchiato</span><span>4.0</span></li>
      <li class="menu-item"><span>Long Macchiato</span><span>4.5</span></li>
      <li class="menu-item"><span>Latte</span><span>4/4.5/5.5</span></li>
      <li class="menu-item"><span>Cappucinno</span><span>4/4.5/5.5</span></li>
      <li class="menu-item"><span>Flat White</span><span>4/4.5/5.5</span></li>
      <li class="menu-item"><span>Long Black</span><span>4/4.5/5.5</span></li>
      <li class="menu-item"><span>Hot Chocolate</span><span>4/4.5/5.5</span></li>
      <li class="menu-item"><span>White Hot Chocolate</span><span>4/4.5/5.5</span></li>
      <li class="menu-item"><span>Mocha</span><span>4.5/5.0/6.0</span></li>
      <li class="menu-item"><span>White Choc Mocha</span><span>4.5/5.0/6.0</span></li>
      <li class="menu-item"><span>Chai Latte</span><span>4.5/5.0/6.0</span></li>
      <li class="menu-item"><span>Dirty Chai</span><span>5.0/5.5/6.5</span></li>
      <li class="menu-item"><span>Selection Of Teas</span><span>3.8</span></li>
    </ul>
  </section>

  <section class="menu-section extras">
    <h2 class="section-title" style="margin-top:0">Extras</h2>
    <ul class="menu-list">
      <li class="menu-item"><span>Extra Shot</span><span>0.5</span></li>
      <li class="menu-item"><span>Decaf</span><span>0.5</span></li>
      <li class="menu-item"><span>Syrups (caramel/hazelnut/vanilla)</span><span>0.5</span></li>
      <li class="menu-item"><span>Soy</span><span>0.5</span></li>
      <li class="menu-item"><span>Lactose Free</span><span>0.5</span></li>
    </ul>
  </section>

  <section class="menu-section cold">
    <h2 class="section-title" style="margin-top:0">Cold Beverages</h2>
    <ul class="menu-list">
      <li class="menu-item"><span>Iced Latte</span><span>4.5</span></li>
      <li class="menu-item"><span>Iced Long Black</span><span>4.5</span></li>
      <li class="menu-item"><span>Iced Coffee W/ice Cream</span><span>6.0</span></li>
      <li class="menu-item"><span>Iced Chocolate W/ice Cream</span><span>6.0</span></li>
      <li class="menu-item"><span>Coffee Frappe</span><span>6.0</span></li>
      <li class="menu-item"><span>Mango Frappe</span><span>6.0</span></li>
    </ul>
  </section>

  <footer class="social">
    <span class="social-dot"></span>
    <span class="social-handle">@wardroundcafe</span>
  </footer>
</main>
</body>
</html>
```